Mediation Website Design Upgrade

Project Details: https://files.plumvaro.net/sheet/k/8Wd3mPzqTuLhXe7nRaBo4_KcVy-92jsQ2fLgNwHd/view?ref=shared

Number of Pages Required

2 page

Font styles to use
Sans Serif

```html
<!DOCTYPE html>
<html lang="en">
<head>
<meta charset="utf-8">
<title>Common Ground Mediation Group</title>
<link href="https://fonts.googleapis.com/css2?family=Nunito:wght@400;600;700&family=Nunito+Sans:wght@400;600&display=swap" rel="stylesheet">
<style>
:root{
  --teal:#4f8a86;
  --teal-dark:#2f6663;
  --green:#6e9a22;
  --green-bright:#74a128;
  --ink:#1d1d1d;
  --body:#555;
  --white:#fff;
}
*{box-sizing:border-box;margin:0;padding:0}
html,body{width:1200px;height:3128px;overflow:hidden;background:var(--white)}
body{position:relative;font-family:"Nunito Sans",sans-serif;color:var(--body)}
.abs{position:absolute}
h1,h2,h3{font-family:"Nunito",sans-serif;font-weight:700;text-transform:uppercase}

/* header */
.site-header{left:0;top:0;width:1200px;height:97px;background:var(--white)}
.brand{display:flex;align-items:center;gap:10px}
.brand-mark{width:22px;height:22px;background:var(--teal)}
.brand-name{font-family:"Nunito",sans-serif;font-weight:700;font-size:17px;color:var(--ink);line-height:1.15}
.site-header .brand{left:90px;top:26px}
.main-nav{left:378px;top:40px;display:flex;gap:30px;font-size:17px;color:var(--ink)}
.main-nav .current{font-weight:700;border-bottom:2px solid var(--ink)}

/* hero */
.hero{left:0;top:97px;width:1200px;height:586px;background:linear-gradient(100deg,#6c7678 0%,#8a8f8c 45%,#a59f96 70%,#c9c0b5 100%)}
.hero-title{left:110px;top:268px;font-size:54px;line-height:48px;color:var(--white)}
.hero-text{left:112px;top:380px;width:440px;font-size:19px;line-height:31px;color:var(--white)}
.arrow{top:340px}

/* service circles */
.service{width:352px;height:352px;border-radius:50%;border:6px solid var(--white);color:var(--white);text-align:center;padding-top:78px}
.service.teal{background:radial-gradient(circle at 50% 40%,#5f9894,#43807c)}
.service.green{background:radial-gradient(circle at 50% 40%,#7fa830,#5f8a1a)}
.service h3{font-size:25px;line-height:29px;font-weight:600;margin-top:14px}
.service p{font-size:12px;line-height:19px;margin:10px auto 0;width:215px}

/* intro */
.photo{border-radius:50%}
.section-title{font-size:33px;line-height:45px;color:var(--ink)}
.rule{height:3px;width:48px;background:var(--teal)}
.copy p{font-size:14px;line-height:23px;color:var(--body);margin-bottom:14px}

/* peace */
.peace-bg{left:0;top:1464px;width:1200px;height:540px}
.peace{left:170px;top:1536px;width:860px;text-align:center;color:var(--white)}
.peace h2{font-size:33px;font-weight:600;color:var(--white)}
.peace .rule{background:var(--white);margin:4px auto 22px;width:40px}
.peace p{font-size:16px;line-height:23px;margin-bottom:14px}
.btn{display:block;font-size:15px;font-weight:600;color:var(--white);text-align:center;text-transform:uppercase}
.btn-solid{background:var(--green-bright);width:280px;height:57px;line-height:57px;margin:22px auto 0}

/* consultation */
.consult{left:150px;top:2570px;width:870px;text-align:center;color:var(--white)}
.consult h2{font-size:29px;font-weight:600}
.consult .rule{background:var(--white);margin:2px auto 20px;width:40px}
.consult p{font-size:19px;line-height:31px}
.btn-outline{border:2px solid var(--white);width:311px;height:55px;line-height:51px;margin:22px auto 0}

/* footer */
.site-footer .brand{left:0;width:1200px;top:2895px;justify-content:center}
.foot-nav{left:0;width:1200px;top:2990px;display:flex;justify-content:center;gap:31px;font-size:17px;color:var(--ink)}
.copyright{left:0;width:1200px;top:3026px;text-align:center;font-size:13px;color:var(--ink)}
.social{left:504px;top:3058px;display:flex;gap:5px}
.social span{width:40px;height:40px;border-radius:50%;border:2px solid var(--green)}
</style>
</head>
<body>

<header class="site-header abs">
  <div class="brand abs"><span class="brand-mark"></span><span class="brand-name">Common Ground<br>Mediation Group</span></div>
  <nav class="main-nav abs">
    <span class="current">Home</span><span>Mediation Services</span><span>Conflict Consulting</span><span>Negotiation</span><span>About Us</span><span>Blog</span><span>Contact</span>
  </nav>
</header>

<section>
  <div class="hero abs" role="img" aria-label="Photo of a tense couple sitting apart on a sofa in a living room"></div>
  <h1 class="hero-title abs">Family<br>Mediation</h1>
  <p class="hero-text abs">Praesent sit amet est In dictum dolor eu dictum porttitor enim felis viverra mi eget</p>
  <svg class="arrow abs" style="left:34px" width="26" height="40" viewBox="0 0 26 40"><path d="M20 4 6 20l14 16" fill="none" stroke="#fff" stroke-width="5"/></svg>
  <svg class="arrow abs" style="left:1146px" width="26" height="40" viewBox="0 0 26 40"><path d="M6 4l14 16L6 36" fill="none" stroke="#fff" stroke-width="5"/></svg>

  <div class="service teal abs" style="left:116px;top:577px">
    <svg width="70" height="70" viewBox="0 0 70 70" fill="none" stroke="#fff" stroke-width="2.5"><circle cx="35" cy="38" r="13"/><path d="M22 38h26M35 25v26M29 27c-4 7-4 15 0 22M41 27c4 7 4 15 0 22"/><circle cx="12" cy="10" r="5"/><circle cx="58" cy="10" r="5"/><circle cx="12" cy="52" r="5"/><circle cx="58" cy="52" r="5"/></svg>
    <h3>Commercial<br>Mediation</h3>
    <p>Praesent sit amet est In dictum dolor eu dictum porttitor enim felis viverra mi eget luctus massa</p>
  </div>
  <div class="service green abs" style="left:425px;top:577px">
    <svg width="80" height="70" viewBox="0 0 80 70" fill="none" stroke="#fff" stroke-width="2.5"><path d="M40 66 10 36C0 26 4 6 20 6c9 0 15 6 20 12 5-6 11-12 20-12 16 0 20 20 10 30Z"/><circle cx="30" cy="30" r="7"/><circle cx="50" cy="30" r="7"/><circle cx="40" cy="44" r="5"/></svg>
    <h3>Family<br>Mediation</h3>
    <p>Praesent sit amet est In dictum dolor eu dictum porttitor enim felis viverra mi eget luctus massa</p>
  </div>
  <div class="service teal abs" style="left:739px;top:577px">
    <svg width="80" height="70" viewBox="0 0 80 70" fill="none" stroke="#fff" stroke-width="2.5"><path d="M8 20v22l18 22M72 20v22L54 64"/><circle cx="32" cy="24" r="6"/><circle cx="48" cy="24" r="6"/><circle cx="40" cy="36" r="5"/><path d="M24 50c0-8 16-8 16 0 0-8 16-8 16 0M40 4v6M28 8l3 5M52 8l-3 5"/></svg>
    <h3>Nonprofits<br>Mediation</h3>
    <p>Praesent sit amet est In dictum dolor eu dictum porttitor enim felis viverra mi eget luctus massa</p>
  </div>
</section>

<section>
  <div class="photo abs" style="left:93px;top:980px;width:426px;height:426px;background:radial-gradient(circle at 55% 40%,#b9a898,#6e6a66 70%,#3d3b3a)" role="img" aria-label="Photo of a worried older woman resting her head on her hand"></div>
  <h2 class="section-title abs" style="left:561px;top:1016px">Have you finally<br>had enough?</h2>
  <div class="rule abs" style="left:561px;top:1108px"></div>
  <div class="copy abs" style="left:562px;top:1135px;width:585px">
    <p>Is there a conflict causing undue stress in your life? Have you and your partner, team or family members reached the tipping point where you need help finding a resolution? It’s okay. Common Ground Mediation Group (CGMG) will help you find the path to a peaceful, satisfying and mutually determined, positive path forward.</p>
    <p>First, know that being in conflict is common in most people’s lives. You and those you are struggling with are far from alone as disputes exist everywhere. When two or more parties feel they aren’t getting anywhere in their discussions and reach an impasse, professional mediation is often the best solution. It saves time, reduces legal costs and can rescue precious relationships.</p>
  </div>
</section>

<section>
  <svg class="peace-bg abs" viewBox="0 0 1200 540" preserveAspectRatio="none" role="img" aria-label="Photo of a smiling family embracing outdoors">
    <defs><linearGradient id="peaceTone" x1="0" y1="0" x2="1" y2="1"><stop offset="0" stop-color="#4a4a2e"/><stop offset=".5" stop-color="#6b6346"/><stop offset="1" stop-color="#3e3a2a"/></linearGradient></defs>
    <path d="M0 0h1200v478c-90 20-200 10-330-20-160-36-300-50-450 10-140 56-300 60-420 0Z" fill="url(#peaceTone)"/>
  </svg>
  <div class="peace abs">
    <h2>Peace is priceless</h2>
    <div class="rule"></div>
    <p>Mediation is a subtle yet organized approach to addressing conflict. It starts with building a platform from which mutually satisfying solutions may evolve. This platform evolves by jointly exploring important factors and desires and clarifying mis-understandings between those who have a stake in the conflict.</p>
    <p>The mediation process is focused on discerning parties’ interests, which are often camouflaged behind assertions and unspoken needs as well as clouded by material demands. Once revealed, clarified and understood, parties can better understand and appreciate each other, and agree to collaborate on how to move forward on resolutions that in many cases benefit everyone involved. Even if a resolution is not achieved, each party more clearly understands the other’s perspective and reasoning.</p>
    <span class="btn btn-solid">Contact us to learn more</span>
  </div>
</section>

<section>
  <h2 class="section-title abs" style="left:125px;top:2096px;font-size:31px;line-height:37px">Traditional and virtual<br>mediation services</h2>
  <div class="rule abs" style="left:128px;top:2181px"></div>
  <div class="copy abs" style="left:128px;top:2205px;width:480px">
    <p style="font-size:15px;line-height:24px">Clients have the option of meeting in person when it suits them or remotely using videoconferencing tools like MeetRoom, TalkLine and CallNest. Online meetings are becoming the norm for many and we are happy to accommodate our clients’ venue preferences whether digital or face to face in a safe setting. In person meetings can be held in our office, a workplace, or even in a family’s living room.</p>
  </div>
  <div class="photo abs" style="left:623px;top:2021px;width:408px;height:408px;background:radial-gradient(circle at 50% 45%,#9aa4b0,#5f6c80 65%,#38475c)" role="img" aria-label="Photo of an older couple arguing on a sofa"></div>
</section>

<section>
  <svg class="abs" style="left:0;top:2493px" width="1200" height="410" viewBox="0 0 1200 410" role="img" aria-label="Photo of a person on a video call, tinted green">
    <defs><linearGradient id="consultTone" x1="0" y1="0" x2="1" y2="0"><stop offset="0" stop-color="#4f8a7a"/><stop offset=".6" stop-color="#679a45"/><stop offset="1" stop-color="#76a52a"/></linearGradient></defs>
    <path d="M0 0h1200v400c-120-20-210-80-380-100-200-22-350 60-520 70C170 378 80 350 0 320Z" fill="url(#consultTone)"/>
  </svg>
  <div class="consult abs">
    <h2>Free 30-minute consultation</h2>
    <div class="rule"></div>
    <p>Are you and another party struggling with a conflict? CGMG offers 30 minutes of initial consultation free by telephone or video conference.</p>
    <span class="btn btn-outline">Schedule your consultation</span>
  </div>
</section>

<footer class="site-footer">
  <div class="brand abs"><span class="brand-mark"></span><span class="brand-name">Common Ground<br>Mediation Group</span></div>
  <nav class="foot-nav abs"><span>Home</span><span>Mediation Services</span><span>Conflict Consulting</span><span>Negotiation</span><span>About Us</span><span>Blog</span><span>Contact</span></nav>
  <p class="copyright abs">© 2020 Company Name | All Rights Reserved</p>
  <div class="social abs" aria-label="Social links"><span></span><span></span><span></span><span></span></div>
</footer>

</body>
</html>
```